Classy business card for accounting firm

We're looking for a new business card for our accounting firm. Our logo was designed by Brandolith, so all of the design info we would like to use has been provided. The specific font provided isn't required to be used.

We want the card to look classy and elegent. Probably more minimalistic, but still with some pops of color.

The options we would like to include on the card are as follows:
1. Main office phone line
2. Direct phone line
3. Email address
4. Website URL
5. Name
6. Title (CEO, President, etc.)
7. Firm Address

The design and card should be double sided!!! The drop down box in the project brief for some reason is defaulting to single sided. Not sure why this is happening.

Thanks!

Contact Information for Business Card

The options we would like to include on the card are as follows: 1. Main office phone line 2. Direct phone line 3. Email address 4. Website URL 5. Name 6. Title (CEO, President, etc.) 7. Firm Address

Requirements
Must have
• Card must be double sided.

```html
<!DOCTYPE html>
<html lang="en">
<head>
<meta charset="utf-8">
<title>Ledgerly Partners – Business Card</title>
<link rel="stylesheet" href="https://fonts.googleapis.com/css2?family=Lato:wght@400;700;900&display=swap">
<style>
  :root {
    --backdrop: #2a2c2f;
    --card: #5e5f60;
    --card-edge: #535455;
    --pattern-a: #5a5b5c;
    --pattern-b: #626364;
    --white: #f4f4f4;
    --muted: #d8d8d8;
    --orange: #f26f1d;
    --green: #a8c23a;
  }
  * { box-sizing: border-box; margin: 0; padding: 0; }
  html, body { width: 1200px; height: 952px; overflow: hidden; }
  body {
    background: var(--backdrop);
    font-family: "Lato", sans-serif;
    display: flex;
    flex-direction: column;
    align-items: center;
    justify-content: center;
    gap: 56px;
  }
  .card {
    position: relative;
    width: 620px;
    height: 354px;
    border-radius: 26px;
    background: var(--card);
    box-shadow: 0 3px 0 var(--card-edge), 0 14px 30px rgba(0,0,0,.45);
    overflow: hidden;
    color: var(--white);
  }

  /* brand block: invented name only, with one plain square */
  .brand-name {
    display: flex; align-items: center; gap: 10px;
    font-weight: 700; letter-spacing: 1.5px; text-transform: uppercase;
    color: var(--white);
  }
  .brand-square { width: 14px; height: 14px; background: var(--orange); }

  /* front */
  .card-front .brand-name { position: absolute; left: 52px; top: 52px; font-size: 19px; }
  .contacts {
    position: absolute; left: 52px; top: 132px;
    list-style: none; display: flex; flex-direction: column; gap: 9px;
    font-size: 13px; line-height: 1.35;
  }
  .contacts li { display: flex; align-items: flex-start; gap: 10px; }
  .contacts svg { flex: none; width: 16px; height: 16px; margin-top: 1px; }
  .person {
    position: absolute; right: 52px; bottom: 78px; text-align: right;
  }
  .person-name { font-size: 22px; font-weight: 900; letter-spacing: 1.5px; text-transform: uppercase; }
  .person-name .given { color: var(--orange); font-weight: 400; }
  .person-name .family { color: var(--green); }
  .person-title {
    display: inline-block; margin-top: 6px; font-size: 14px; color: var(--white);
    padding-bottom: 5px; border-bottom: 2px solid var(--orange);
  }

  /* back */
  .pattern-field {
    position: absolute; inset: 0;
    background: linear-gradient(135deg, var(--pattern-b), var(--pattern-a) 60%, var(--pattern-b));
  }
  .card-back .brand-name {
    position: absolute; left: 0; right: 0; top: 204px;
    justify-content: center; font-size: 22px;
  }
</style>
</head>
<body>

  <section class="card card-front" aria-label="Card front">
    <div class="brand-name"><span class="brand-square"></span>Ledgerly Partners</div>

    <ul class="contacts">
      <li>
        <svg viewBox="0 0 16 16" aria-hidden="true"><rect width="16" height="16" rx="2" fill="var(--orange)"/><path d="M8 3.2a3 3 0 0 0-3 3c0 2.3 3 6.3 3 6.3s3-4 3-6.3a3 3 0 0 0-3-3z" fill="#fff"/><circle cx="8" cy="6.2" r="1.1" fill="var(--orange)"/></svg>
        <span>1720 Maple Crest Avenue<br>Arlington, VA 22201</span>
      </li>
      <li>
        <svg viewBox="0 0 16 16" aria-hidden="true"><rect width="16" height="16" rx="2" fill="var(--green)"/><path d="M5 3.5l1.8 2-1 1.2a6 6 0 0 0 3.5 3.5l1.2-1 2 1.8-1 1.5c-3.8 0-7.5-3.7-7.5-7.5z" fill="#fff"/></svg>
        <span>+00 987 654 32</span>
      </li>
      <li>
        <svg viewBox="0 0 16 16" aria-hidden="true"><rect width="16" height="16" rx="2" fill="var(--green)"/><rect x="3" y="4.5" width="10" height="7" fill="#fff"/><path d="M3 4.5l5 4 5-4" fill="none" stroke="var(--green)" stroke-width="1"/></svg>
        <span>hello@ledgerlypartners.com</span>
      </li>
      <li>
        <svg viewBox="0 0 16 16" aria-hidden="true"><rect width="16" height="16" rx="2" fill="var(--green)"/><path d="M5 4l7 3.2-3 .9 2.4 3-1.2 1-2.4-3-1.8 2.4z" fill="#fff"/></svg>
        <span>www.ledgerlypartners.com</span>
      </li>
    </ul>

    <div class="person">
      <div class="person-name"><span class="given">Daniel R.</span> <span class="family">Holloway</span></div>
      <div class="person-title">Managing Director</div>
    </div>
  </section>

  <section class="card card-back" aria-label="Card back">
    <div class="pattern-field" role="img" aria-label="Tone-on-tone repeating brand pattern across the card"></div>
    <div class="brand-name"><span class="brand-square"></span>Ledgerly Partners</div>
  </section>

</body>
</html>
```